PVQ BOOK COVER 6 X 9 - MARKET LEADING LEADERSHIP BOOK

I need a book cover designed for a book called Steering Through the Era of Circuits – Enduring Insight for an Automated Century and some more stuff, which you can see in the image I generated. I created a basic cover, but it needs to wow; it's about leadership, ancient wisdom, and AI. This book offers a unique approach: combining 2,000-year-old Stoic philosophy with practical frameworks for modern AI-age leadership challenges. Rather than another technical book about AI, this is a deeply human guide for leaders who want to harness AI's power while preserving their organisation's humanity.

Target Market(s)

EXECUTIVES, LEADERS MANAGERS DEALING WITH AI

Industry/Entity Type

LEADERSHIP

Requirements
Must have
• MUSIC BE CLASSY AND A SOLID COMBINATION OF ANCIENT WISDOM AND FUTURISTIC AI
Nice to have
• GIVE ME THE BEST YOU HAVE
Should not have
• NON

```html
<!DOCTYPE html>
<html lang="en">
<head>
<meta charset="utf-8">
<title>Steering Through the Era of Circuits – Book Cover</title>
<link rel="stylesheet" href="https://fonts.googleapis.com/css2?family=Cinzel:wght@500;600&family=Montserrat:wght@500;600&display=swap">
<style>
  :root {
    --page: #ffffff;
    --navy: #0a1a26;
    --cream: #f3ecd8;
    --gold: #e9b023;
    --gold-line: #c9971f;
    --ring: rgba(201, 151, 31, 0.35);
    --bronze-glow: rgba(150, 98, 36, 0.55);
    --bronze-fade: rgba(110, 70, 26, 0.22);
  }
  * { margin: 0; padding: 0; box-sizing: border-box; }
  html, body {
    width: 1200px;
    height: 1200px;
    overflow: hidden;
    background: var(--page);
  }
  .canvas {
    position: relative;
    width: 1200px;
    height: 1200px;
    background: var(--page);
  }
  .cover {
    position: absolute;
    left: 222px;
    top: 31px;
    width: 764px;
    height: 1146px;
    background: var(--navy);
    overflow: hidden;
  }
  .rings {
    position: absolute;
    left: 0;
    top: 0;
  }
  .portrait-art {
    position: absolute;
    left: 112px;
    top: 370px;
    width: 540px;
    height: 520px;
    background: radial-gradient(ellipse 50% 50% at 50% 50%, var(--bronze-glow) 0%, var(--bronze-fade) 55%, rgba(10, 26, 38, 0) 100%);
  }
  .title {
    position: absolute;
    left: 0;
    width: 100%;
    text-align: center;
    font-family: "Cinzel", "Trajan Pro", serif;
    font-weight: 500;
    color: var(--cream);
    line-height: 1;
    white-space: nowrap;
  }
  .title-main {
    top: 37px;
    font-size: 125px;
    letter-spacing: 1px;
  }
  .title-mid {
    top: 167px;
    font-size: 56px;
    letter-spacing: 1px;
  }
  .title-end {
    top: 249px;
    font-size: 125px;
    letter-spacing: 1px;
  }
  .subtitle {
    position: absolute;
    left: 0;
    top: 745px;
    width: 100%;
    text-align: center;
    font-family: "Montserrat", Arial, sans-serif;
    font-weight: 600;
    font-size: 31px;
    line-height: 44px;
    letter-spacing: 6px;
    color: var(--gold);
  }
  .rule {
    position: absolute;
    left: 90px;
    width: 574px;
    height: 2px;
    background: var(--gold-line);
  }
  .rule-top { top: 856px; }
  .rule-bottom { top: 978px; }
  .tagline {
    position: absolute;
    left: 0;
    top: 861px;
    width: 100%;
    text-align: center;
    font-family: "Montserrat", Arial, sans-serif;
    font-weight: 500;
    font-size: 25px;
    line-height: 36.5px;
    letter-spacing: 2.5px;
    color: var(--cream);
  }
  .tagline .small { font-size: 19px; }
  .author {
    position: absolute;
    left: 0;
    top: 1017px;
    width: 100%;
    text-align: center;
    font-family: "Cinzel", "Trajan Pro", serif;
    font-weight: 500;
    font-size: 75px;
    line-height: 1;
    color: var(--cream);
    letter-spacing: 1px;
    white-space: nowrap;
  }
</style>
</head>
<body>
<main class="canvas">
  <section class="cover">
    <svg class="rings" width="764" height="1146" viewBox="0 0 764 1146" aria-hidden="true">
      <g fill="none" stroke="var(--ring)" stroke-width="1.2">
        <circle cx="381" cy="572" r="292"/>
        <circle cx="381" cy="572" r="242"/>
        <circle cx="381" cy="572" r="192"/>
        <circle cx="381" cy="572" r="142"/>
      </g>
    </svg>
    <div class="portrait-art" role="img" aria-label="Bronze-toned classical bust of a bearded Stoic philosopher in profile, draped in a toga"></div>

    <h1 class="title title-main">STEERING</h1>
    <p class="title title-mid">THROUGH THE ERA OF</p>
    <p class="title title-end">CIRCUITS</p>

    <p class="subtitle">ENDURING INSIGHT FOR AN<br>AUTOMATED CENTURY</p>

    <div class="rule rule-top"></div>
    <p class="tagline">
      STOIC STRATEGY, ETHICAL CLARITY,<br>
      <span class="small">AND</span> HUMAN LEADERSHIP <span class="small">IN THE RISE</span><br>
      <span class="small">OF</span> ARTIFICIAL INTELLIGENCE
    </p>
    <div class="rule rule-bottom"></div>

    <p class="author">RAVINDER HALE</p>
  </section>
</main>
</body>
</html>
```